Mobile Oil Change company needs a flyer to promote new business

We need a flyer to 1) print & handout and 2) email out to potential customers. We are a mobile oil change company that comes to our customer locations to perform the work instead of customers going to traditional oil change companies. We have a 21 point inspection with our oil change. (21 point inspection details will not be on the flyer). Would like to keep the flyer simple but creative. I'm attaching 1) the write-up we created, 2) our logo (logo color is dark teal on white but other combinations are included if you wanted to propose a different color combination), and 3) additional services we offer. Logo font is Alegreya Sans.
Would like the additional services listed with icons and brief descriptions (similar to attachment) without pricing. Company website for reference is www.brookmerelubeworks.com.

Target Market(s)

Companies with many service vehicles such as Oil & Gas service companies, heating and air conditioning companies, utility companies, police departments, etc. Companies that prioritize convenience and maintenance first.

Font styles to use
Sans Serif

Colors
00a990

Requirements
Must have
• Simple but creative design with our logo at top of the flyer. Additional Services (details in document supplied) can be smaller and less prominent than other "main" content listed in the CONTENT document supplied.
Should not have
• Do not use animated character graphics in the flyer and limit (1) stock photos to A small area in the flyer.

```html
<!DOCTYPE html>
<html lang="en">
<head>
<meta charset="utf-8">
<title>Brookmere Lube Works – Mobile Oil Change Flyer</title>
<link href="https://fonts.googleapis.com/css2?family=Alegreya+Sans:wght@700;800&family=Roboto:wght@400;500;700&display=swap" rel="stylesheet">
<style>
  :root{
    --page-bg:#e2e2e2;
    --paper:#ffffff;
    --ink-dark:#17474c;
    --brand-green:#00a990;
    --band-teal:#1ac5ad;
    --panel-ice:#b3f1f6;
    --text-body:#1f2b2d;
    --white:#ffffff;
    --icon-line:#39b9c6;
  }
  *{box-sizing:border-box;margin:0;padding:0}
  html,body{width:1200px;height:1200px;overflow:hidden;background:var(--page-bg)}
  body{font-family:'Roboto',sans-serif;position:relative}
  .flyer{
    position:absolute;left:225px;top:75px;width:750px;height:1050px;
    background:var(--paper);transform:scale(1.12);transform-origin:center;overflow:hidden;
  }
  .abs{position:absolute}
  .brand-name{
    left:0;right:0;top:48px;text-align:center;
    font-family:'Alegreya Sans',sans-serif;font-weight:800;font-size:36px;
    color:var(--ink-dark);letter-spacing:.5px;
  }
  .headline{left:0;right:0;top:138px;text-align:center;font-family:'Alegreya Sans',sans-serif;font-weight:800;line-height:55px}
  .headline .line-one{display:block;font-size:49px;color:var(--ink-dark)}
  .headline .line-two{display:block;font-size:49px;color:var(--brand-green)}
  .process-band{left:0;top:262px;width:750px;height:442px;background:var(--band-teal)}
  .band-rule{left:0;top:704px;width:750px;height:11px;background:var(--ink-dark)}
  .hero-art{
    left:0;top:292px;width:335px;height:372px;
    background:linear-gradient(160deg, #f7b719 0%, #e8394a 55%, #36b3bf 100%);
    opacity:.35;border-radius:10px;
  }
  .process-intro{
    left:351px;top:304px;width:366px;color:var(--white);
    font-size:24px;line-height:23.5px;text-align:justify;text-align-last:left;
  }
  .steps{left:351px;top:414px;width:380px}
  .steps-line{left:366px;top:430px;width:3px;height:205px;background:var(--ink-dark)}
  .step{position:absolute;left:0;display:flex;align-items:center;width:380px}
  .step-num{
    flex:0 0 34px;height:34px;border-radius:50%;background:var(--ink-dark);
    border:2px solid var(--band-teal);box-shadow:0 0 0 1px var(--ink-dark);
    color:var(--white);font-size:17px;display:flex;align-items:center;justify-content:center;
  }
  .step-text{margin-left:11px;color:var(--white);font-size:18px;line-height:22px}
  .benefits{left:30px;top:752px;width:350px;list-style:none;color:var(--text-body);font-size:18px;line-height:22px}
  .benefits li{position:relative;padding-left:27px;margin-bottom:7px}
  .benefits svg{position:absolute;left:0;top:3px}
  .call-label{left:32px;top:870px;display:flex;align-items:center;gap:12px;font-size:24px;font-weight:500;color:var(--ink-dark)}
  .phone-box{left:0;top:906px;width:308px;height:51px;background:var(--ink-dark);color:var(--white);font-size:31px;font-weight:500;padding-left:32px;line-height:51px}
  .extras-panel{left:391px;top:715px;width:359px;height:295px;background:var(--panel-ice)}
  .extras-title{left:414px;top:751px;font-size:18px;font-weight:500;color:var(--ink-dark)}
  .extra{position:absolute;display:flex;align-items:center;width:160px}
  .extra-icon{flex:0 0 36px;height:36px;border-radius:50%;background:var(--white);display:flex;align-items:center;justify-content:center}
  .extra-text{margin-left:10px;font-size:12.5px;font-weight:700;line-height:15px;color:var(--ink-dark);white-space:nowrap}
  .footer-shapes{left:0;top:960px}
  .contact{left:448px;top:972px;color:var(--white);font-size:16px;line-height:25px;white-space:nowrap}
  .contact div{display:flex;align-items:center;gap:12px}
</style>
</head>
<body>
<main class="flyer">
  <div class="abs brand-name">Brookmere Lube Works</div>
  <h1 class="abs headline"><span class="line-one">HASSLE FREE OIL CHANGES</span><span class="line-two">ON YOUR TERMS</span></h1>

  <section class="abs process-band"></section>
  <div class="abs hero-art" role="img" aria-label="Illustration of a mechanic in overalls refuelling a red car beside a yellow service pump"></div>
  <p class="abs process-intro">Our simple 5-step process lets you schedule an appointment and get service to save time and money:</p>
  <div class="abs steps-line"></div>
  <div class="abs steps">
    <div class="step" style="top:0"><span class="step-num">01</span><span class="step-text">Call or email us to schedule service</span></div>
    <div class="step" style="top:42px"><span class="step-num">02</span><span class="step-text">Our highly trained technicians come to you for service</span></div>
    <div class="step" style="top:93px"><span class="step-num">03</span><span class="step-text">Service is performed quickly on your vehicle</span></div>
    <div class="step" style="top:149px"><span class="step-num">04</span><span class="step-text">Pay agreed-upon pricing and receipt is emailed to you</span></div>
    <div class="step" style="top:203px"><span class="step-num">05</span><span class="step-text">Services performed are tracked electronically and reminders created</span></div>
  </div>
  <div class="abs band-rule"></div>

  <ul class="abs benefits">
    <li><svg width="18" height="16" viewBox="0 0 18 16"><path d="M1 9l5 5L17 2" fill="none" stroke="#1f2b2d" stroke-width="3"/></svg>High quality synthetic oil used is best suited for commercial vehicles</li>
    <li><svg width="18" height="16" viewBox="0 0 18 16"><path d="M1 9l5 5L17 2" fill="none" stroke="#1f2b2d" stroke-width="3"/></svg>Service includes a 21-point inspection</li>
    <li><svg width="18" height="16" viewBox="0 0 18 16"><path d="M1 9l5 5L17 2" fill="none" stroke="#1f2b2d" stroke-width="3"/></svg>Additional services are available</li>
  </ul>
  <div class="abs call-label">
    <svg width="30" height="30" viewBox="0 0 30 30"><path d="M7 3l5 6-3 3c2 4 5 7 9 9l3-3 6 5-3 4C14 27 3 16 3 6z" fill="var(--brand-green)"/><path d="M18 4a9 9 0 0 1 8 8M18 9a4 4 0 0 1 3 3" fill="none" stroke="var(--brand-green)" stroke-width="2.2"/></svg>
    CALL NOW AT
  </div>
  <div class="abs phone-box">(833) 5-BLW-OIL</div>

  <section class="abs extras-panel"></section>
  <h2 class="abs extras-title">Additional Services</h2>
  <div class="extra" style="left:414px;top:785px"><span class="extra-icon"><svg width="18" height="18"><rect x="2" y="2" width="14" height="14" fill="none" stroke="#39b9c6" stroke-width="2"/><path d="M6 3v12M9 3v12M12 3v12" stroke="#39b9c6"/></svg></span><span class="extra-text">Engine Air Filter<br>Replacement</span></div>
  <div class="extra" style="left:576px;top:785px"><span class="extra-icon"><svg width="18" height="18"><path d="M3 4h12M3 8h12M3 12h12M5 16h8" stroke="#39b9c6" stroke-width="1.6"/></svg></span><span class="extra-text">Cabin Air Filter<br>Replacement</span></div>
  <div class="extra" style="left:414px;top:840px"><span class="extra-icon"><svg width="18" height="18"><path d="M2 7c4-4 10-4 14 0L9 15z" fill="none" stroke="#39b9c6" stroke-width="1.6"/></svg></span><span class="extra-text">Wiperblade<br>Replacement</span></div>
  <div class="extra" style="left:576px;top:840px"><span class="extra-icon"><svg width="20" height="20"><circle cx="10" cy="10" r="8" fill="none" stroke="#39b9c6" stroke-width="1.6"/><circle cx="10" cy="10" r="3" fill="none" stroke="#39b9c6" stroke-width="1.6"/></svg></span><span class="extra-text">Power Steering<br>Fluid Flush</span></div>
  <div class="extra" style="left:414px;top:896px"><span class="extra-icon"><svg width="18" height="18"><rect x="3" y="2" width="8" height="14" fill="none" stroke="#39b9c6" stroke-width="1.6"/><path d="M11 6h3v8" fill="none" stroke="#39b9c6" stroke-width="1.6"/></svg></span><span class="extra-text">Fuel System<br>Treatment</span></div>
  <div class="extra" style="left:576px;top:896px"><span class="extra-icon"><svg width="20" height="20"><circle cx="10" cy="10" r="8" fill="none" stroke="#39b9c6" stroke-width="1.6"/><path d="M10 2v16M2 10h16" stroke="#39b9c6" stroke-width="1.2"/></svg></span><span class="extra-text">Brake Fluid<br>Flush</span></div>

  <svg class="abs footer-shapes" width="750" height="90" viewBox="0 0 750 90">
    <rect x="0" y="47" width="420" height="5" fill="var(--brand-green)"/>
    <rect x="0" y="57" width="750" height="13" fill="var(--ink-dark)"/>
    <path d="M430 4H750V70H415z" fill="var(--ink-dark)"/>
  </svg>
  <div class="abs contact">
    <div><svg width="20" height="14"><rect x="1" y="1" width="18" height="12" fill="none" stroke="#fff" stroke-width="1.5"/><path d="M1 1l9 7 9-7" fill="none" stroke="#fff" stroke-width="1.5"/></svg>Sales@BrookmereLubeWorks.com</div>
    <div><svg width="20" height="20"><circle cx="10" cy="10" r="8" fill="none" stroke="#fff" stroke-width="1.5"/><ellipse cx="10" cy="10" rx="3.5" ry="8" fill="none" stroke="#fff" stroke-width="1.2"/><path d="M2 10h16M3.5 6h13M3.5 14h13" stroke="#fff" stroke-width="1.2"/></svg>www.brookmerelubeworks.com</div>
  </div>
</main>
</body>
</html>
```